Business Card Design

Melodex Podcast

Industry/Entity Type

Business

Contact Information for Business Card

YOU ARE INVITED TO LISTEN
Stretch Every Idea
Award Winning Melodex Podcast
with Dr. Marla Quenby
www.drmarlaquenby-example.com

555-018-7364

```html
<!DOCTYPE html>
<html lang="en">
<head>
<meta charset="utf-8">
<title>Melodex Podcast – Business Card</title>
<link rel="stylesheet" href="https://fonts.googleapis.com/css2?family=Tenor+Sans&family=Questrial&family=Crimson+Text&family=PT+Sans&display=swap">
<style>
  :root {
    --page-bg: #e4e4e4;
    --panel-dark: #242424;
    --accent-lime: #b8d430;
    --accent-soft: #c4dc6e;
    --band-green: #6e9a3a;
    --name-white: #ffffff;
    --photo-light: #c9e27a;
    --photo-mid: #a8cf4a;
    --photo-deep: #86b33a;
  }
  * { box-sizing: border-box; margin: 0; padding: 0; }
  html, body {
    width: 1200px;
    height: 1000px;
    overflow: hidden;
    background: var(--page-bg);
  }
  .card {
    position: absolute;
    left: 175px;
    top: 260px;
    width: 840px;
    height: 492px;
    display: flex;
  }
  .card__info {
    position: relative;
    width: 446px;
    height: 100%;
    background: var(--panel-dark);
    overflow: hidden;
  }
  .card__headline {
    position: absolute;
    top: 74px;
    left: 30px;
    right: 0;
    text-align: center;
    font-family: "Tenor Sans", sans-serif;
    font-weight: 400;
    font-size: 40px;
    line-height: 48px;
    color: var(--accent-lime);
  }
  .card__tagline {
    position: absolute;
    top: 202px;
    left: 20px;
    right: 0;
    text-align: center;
    font-family: "Questrial", sans-serif;
    font-size: 19px;
    line-height: 29px;
    color: var(--accent-soft);
  }
  .card__name-band {
    position: absolute;
    top: 292px;
    left: 0;
    width: 100%;
    height: 60px;
    background: var(--band-green);
    display: flex;
    align-items: center;
    justify-content: center;
  }
  .card__name {
    font-family: "Crimson Text", serif;
    font-size: 35px;
    color: var(--name-white);
  }
  .card__contact {
    position: absolute;
    top: 400px;
    left: 0;
    right: 0;
    display: flex;
    align-items: center;
    justify-content: center;
    gap: 7px;
    font-family: "PT Sans", sans-serif;
    font-size: 17px;
    color: var(--accent-lime);
    white-space: nowrap;
  }
  .card__contact-dot {
    width: 9px;
    height: 9px;
    border-radius: 50%;
    background: var(--accent-lime);
  }
  .card__photo {
    flex: 1;
    height: 100%;
    background: radial-gradient(circle at 40% 20%, var(--photo-light), var(--photo-mid) 55%, var(--photo-deep));
  }
</style>
</head>
<body>
  <div class="card">
    <section class="card__info">
      <h1 class="card__headline">YOU ARE INVITED<br>TO LISTEN</h1>
      <p class="card__tagline">Stretch Every Idea Award Winning<br>Melodex Podcast with</p>
      <div class="card__name-band">
        <span class="card__name">Dr. Marla Quenby</span>
      </div>
      <p class="card__contact">
        <span class="card__contact-web">www.drmarlaquenby-example.com</span>
        <span class="card__contact-dot"></span>
        <span class="card__contact-phone">555-018-7364</span>
      </p>
    </section>
    <div class="card__photo" role="img" aria-label="Photo of a chrome vintage studio microphone against a lime green background"></div>
  </div>
</body>
</html>
```